A new novel about the early days of The Marlows needs a book cover design

The title of the book is A LANTERN IN WINTER
The cover should also include "a novel" and "by Tom Holloway" Those can be together or separate.
The design element I'd like to incorporate is the iconic "Dock Wall" photo of The Marlows in 1960, which I've attached below. Since we're not sure if we can get the rights to the actual photo, it's probably best if the design merely references that photo, or distorts it in an interesting way. But it should be very clear that the book is about the Marlows.
The novel is in many ways based on that photo and evokes the city of Hamburg in 1960, which was gritty, raw, and sexually charged (as were The Marlows).
The tone of the novel is romantic, passionate, and very funny - but never broad and silly.

```html
<!DOCTYPE html>
<html lang="en">
<head>
<meta charset="utf-8">
<title>A Lantern in Winter — Book Cover</title>
<link href="https://fonts.googleapis.com/css2?family=Abril+Fatface&family=Courier+Prime&display=swap" rel="stylesheet">
<style>
  :root {
    --backdrop: #e8e6e3;
    --paper: #ffffff;
    --ink: #111111;
    --photo-shadow: #161616;
    --photo-dark: #2b2b2b;
    --photo-mid: #555555;
    --photo-grass: #8f8f8f;
    --photo-light: #b4b4b4;
  }
  html, body {
    margin: 0;
    padding: 0;
    width: 1200px;
    height: 950px;
    overflow: hidden;
    background: var(--backdrop);
  }
  .canvas {
    width: 1200px;
    height: 950px;
    display: flex;
    align-items: center;
    justify-content: center;
  }
  .book-cover {
    width: 640px;
    height: 900px;
    background: var(--paper);
    box-shadow: 0 6px 22px rgba(0,0,0,0.18);
  }
  .cover-art {
    display: block;
    width: 640px;
    height: 900px;
  }
  .title-lead {
    font-family: "Abril Fatface", serif;
    fill: var(--ink);
  }
  .title-shape text {
    font-family: "Abril Fatface", serif;
  }
  .title-ink { fill: var(--ink); }
  .tagline,
  .author {
    font-family: "Courier Prime", monospace;
    fill: var(--ink);
  }
</style>
</head>
<body>
<main class="canvas">
  <article class="book-cover">
    <svg class="cover-art" viewBox="0 0 640 900" xmlns="http://www.w3.org/2000/svg">
      <defs>
        <clipPath id="title-shape" class="title-shape">
          <text x="70" y="300" font-size="205" textLength="500" lengthAdjust="spacingAndGlyphs">LANTERN</text>
          <text x="70" y="455" font-size="205" textLength="210" lengthAdjust="spacingAndGlyphs">IN</text>
          <text x="70" y="610" font-size="205" textLength="500" lengthAdjust="spacingAndGlyphs">WINTER</text>
        </clipPath>
        <linearGradient id="photo-tones" x1="0" y1="0" x2="0" y2="1">
          <stop offset="0" stop-color="var(--photo-dark)"/>
          <stop offset="0.2" stop-color="var(--photo-mid)"/>
          <stop offset="0.38" stop-color="var(--photo-shadow)"/>
          <stop offset="0.55" stop-color="var(--photo-dark)"/>
          <stop offset="0.68" stop-color="var(--photo-grass)"/>
          <stop offset="0.85" stop-color="var(--photo-light)"/>
          <stop offset="1" stop-color="var(--photo-grass)"/>
        </linearGradient>
      </defs>

      <text class="title-lead" x="400" y="150" font-size="92">A</text>

      <g class="title" clip-path="url(#title-shape)">
        <rect class="title-ink" x="0" y="140" width="640" height="100"/>
        <rect class="title-photo" x="0" y="225" width="640" height="400" fill="url(#photo-tones)"
              role="img" aria-label="Placeholder for the Dock Wall photograph of The Marlows in Hamburg, 1960, seen through the title letters"/>
      </g>

      <text class="tagline" x="72" y="690" font-size="28">a novel</text>
      <text class="author" x="72" y="790" font-size="46">by Tom Holloway</text>
    </svg>
  </article>
</main>
</body>
</html>
```